Tidewell Partners Inc.
Business Card & Stationary
Tidewell Partners Inc. -
Creative Brief
Professional
Derek Holloway
President & CEO
47 Quillfern Lane Brackenford, Lakeshire, Canada M4R 7P9
derek@tidewellpartners.example
www.tidewellpartners.example
needs to be top drawer, classy, printing costs not a key factor
Guiding Leaders Toward Lasting Momentum in Revenue

```html
<!DOCTYPE html>
<html lang="en">
<head>
<meta charset="utf-8">
<title>Tidewell Partners Inc. — Business Card &amp; Stationery</title>
<link rel="stylesheet" href="https://fonts.googleapis.com/css2?family=Open+Sans:wght@400;600;700&display=swap">
<style>
  :root {
    --bg: #e9ebee;
    --paper: #ffffff;
    --blue-deep: #0b3f8c;
    --blue: #1565c0;
    --blue-bright: #2a8ae0;
    --blue-pale: #cfe3f7;
    --ink: #3a4452;
    --ink-soft: #7a8594;
    --shadow: rgba(20, 40, 70, 0.18);
  }
  * { box-sizing: border-box; margin: 0; padding: 0; }
  html, body { width: 1200px; height: 701px; overflow: hidden; }
  body {
    background: var(--bg);
    font-family: "Open Sans", Arial, sans-serif;
    color: var(--ink);
    position: relative;
  }
  .piece {
    position: absolute;
    background: var(--paper);
    box-shadow: 0 6px 18px var(--shadow);
    overflow: hidden;
  }
  .piece svg.band { position: absolute; left: 0; top: 0; }

  /* brand name (logo stand-in) */
  .brand { display: flex; align-items: center; gap: 7px; position: absolute; }
  .brand-square { width: 14px; height: 14px; background: var(--blue); flex: none; }
  .brand-name { font-weight: 700; color: var(--blue); font-size: 14px; letter-spacing: 0.2px; white-space: nowrap; }
  .brand.on-dark .brand-square { background: var(--paper); }
  .brand.on-dark .brand-name { color: var(--paper); }

  .person-name { font-weight: 700; color: var(--blue); font-size: 13px; white-space: nowrap; }
  .person-title { font-size: 8px; color: var(--ink-soft); }
  .small { font-size: 7.5px; line-height: 1.45; white-space: nowrap; }
  .white { color: var(--paper); }

  /* business card front */
  .card-front { left: 30px; top: 110px; width: 300px; height: 171px; }
  .card-front .brand { left: 16px; top: 22px; gap: 5px; }
  .card-front .brand-name { font-size: 10px; }
  .card-front .brand-square { width: 9px; height: 9px; }
  .card-front .person { position: absolute; right: 16px; top: 12px; text-align: right; padding-right: 8px; border-right: 2px solid var(--blue); }
  .card-front .person-name { font-size: 12px; }
  .card-front .address { position: absolute; left: 16px; top: 68px; }
  .card-front .phones { position: absolute; left: 150px; top: 68px; }
  .card-front .web { position: absolute; left: 16px; top: 124px; color: var(--ink); }
  .card-front .web b { color: var(--blue); }

  /* business card back */
  .card-back { left: 30px; top: 320px; width: 300px; height: 171px; background: linear-gradient(135deg, var(--blue-bright), var(--blue-deep)); }
  .card-back .brand { left: 60px; top: 62px; }
  .card-back .brand-name { font-size: 15px; }
  .card-back .tagline { position: absolute; left: 0; right: 0; top: 96px; text-align: center; color: var(--paper); font-size: 8.5px; font-weight: 600; }
  .card-back .foot-line { position: absolute; left: 0; right: 0; bottom: 12px; height: 3px; background: var(--blue-pale); }

  /* letterhead */
  .letterhead { left: 370px; top: 60px; width: 420px; height: 560px; }
  .letterhead .brand { left: 28px; top: 30px; }
  .letterhead .brand-name { font-size: 17px; }
  .letterhead .person { position: absolute; right: 28px; top: 86px; text-align: right; }
  .letterhead .person .person-name { color: var(--paper); }
  .letterhead .person .person-title { color: var(--blue-pale); }
  .letterhead .footer { position: absolute; left: 28px; right: 28px; bottom: 28px; display: flex; gap: 22px; border-top: 1px solid var(--blue-pale); padding-top: 10px; }
  .letterhead .footer b { color: var(--blue); }

  /* #10 envelope */
  .envelope-long { left: 820px; top: 90px; width: 350px; height: 152px; }
  .envelope-long .web { position: absolute; right: 18px; top: 14px; font-size: 9px; font-weight: 600; }

  /* square-flap envelope */
  .envelope-small { left: 820px; top: 300px; width: 350px; height: 200px; }
  .envelope-small .brand { left: 22px; top: 78px; }
  .envelope-small .brand-name { font-size: 15px; }
  .envelope-small .return { position: absolute; left: 22px; top: 104px; color: var(--ink-soft); }
</style>
</head>
<body>

  <section class="piece card-front" aria-label="Business card front">
    <svg class="band" width="300" height="171" viewBox="0 0 300 171" aria-hidden="true">
      <defs>
        <linearGradient id="cardBand" x1="0" y1="0" x2="1" y2="0">
          <stop offset="0" stop-color="#0b3f8c"/>
          <stop offset="0.6" stop-color="#1565c0"/>
          <stop offset="1" stop-color="#2a8ae0"/>
        </linearGradient>
      </defs>
      <path d="M0 58 L300 58 L300 112 Q150 104 0 118 Z" fill="url(#cardBand)"/>
      <rect x="0" y="52" width="300" height="2" fill="#cfe3f7"/>
    </svg>
    <div class="brand"><span class="brand-square"></span><span class="brand-name">Tidewell Partners Inc.</span></div>
    <div class="person">
      <div class="person-name">Derek Holloway</div>
      <div class="person-title">President &amp; CEO</div>
    </div>
    <div class="address small white">47 Quillfern Lane<br>Brackenford, Lakeshire, Canada<br>M4R 7P9</div>
    <div class="phones small white">Phone: 555.014.2286<br>Cell: 555.018.7626<br>Fax: 555.016.3591</div>
    <div class="web small">Email: derek@tidewellpartners.example<br>Web: <b>www.tidewellpartners.example</b></div>
  </section>

  <section class="piece card-back" aria-label="Business card back">
    <div class="brand on-dark"><span class="brand-square"></span><span class="brand-name">Tidewell Partners Inc.</span></div>
    <p class="tagline">Guiding Leaders Toward Lasting Momentum in Revenue</p>
    <div class="foot-line"></div>
  </section>

  <section class="piece letterhead" aria-label="Letterhead">
    <svg class="band" width="420" height="140" viewBox="0 0 420 140" aria-hidden="true">
      <defs>
        <linearGradient id="letterBand" x1="0" y1="0" x2="1" y2="0">
          <stop offset="0" stop-color="#cfe3f7"/>
          <stop offset="0.45" stop-color="#2a8ae0"/>
          <stop offset="1" stop-color="#0b3f8c"/>
        </linearGradient>
      </defs>
      <path d="M0 74 Q210 56 420 64 L420 124 Q210 108 0 132 Z" fill="url(#letterBand)"/>
      <path d="M0 136 Q210 112 420 128" fill="none" stroke="#cfe3f7" stroke-width="2"/>
    </svg>
    <div class="brand"><span class="brand-square"></span><span class="brand-name">Tidewell Partners Inc.</span></div>
    <div class="person">
      <div class="person-name">Derek Holloway</div>
      <div class="person-title">President &amp; CEO</div>
    </div>
    <div class="footer small">
      <div>47 Quillfern Lane<br>Brackenford, Lakeshire<br>Canada M4R 7P9</div>
      <div>Phone: 555.014.2286<br>Cell: 555.018.7626<br>Fax: 555.016.3591</div>
      <div>Email: derek@tidewellpartners.example<br>Web: <b>www.tidewellpartners.example</b></div>
    </div>
  </section>

  <section class="piece envelope-long" aria-label="Envelope">
    <svg class="band" width="350" height="152" viewBox="0 0 350 152" aria-hidden="true">
      <defs>
        <linearGradient id="envBand" x1="0" y1="0" x2="1" y2="0">
          <stop offset="0" stop-color="#2a8ae0"/>
          <stop offset="1" stop-color="#0b3f8c"/>
        </linearGradient>
      </defs>
      <path d="M150 0 L350 0 L350 44 Q260 32 120 40 Q150 20 150 0 Z" fill="url(#envBand)"/>
    </svg>
    <div class="web white">www.tidewellpartners.example</div>
  </section>

  <section class="piece envelope-small" aria-label="Envelope with return address">
    <svg class="band" width="350" height="200" viewBox="0 0 350 200" aria-hidden="true">
      <defs>
        <linearGradient id="smallBand" x1="0" y1="0" x2="1" y2="0">
          <stop offset="0" stop-color="#cfe3f7"/>
          <stop offset="0.4" stop-color="#2a8ae0"/>
          <stop offset="1" stop-color="#0b3f8c"/>
        </linearGradient>
      </defs>
      <path d="M0 18 Q175 4 350 12 L350 60 Q175 50 0 66 Z" fill="url(#smallBand)"/>
      <path d="M0 70 Q175 54 350 64" fill="none" stroke="#cfe3f7" stroke-width="2"/>
    </svg>
    <div class="brand"><span class="brand-square"></span><span class="brand-name">Tidewell Partners Inc.</span></div>
    <div class="return small">47 Quillfern Lane Brackenford, Lakeshire, Canada<br>M4R 7P9</div>
  </section>

</body>
</html>
```